Guarenteed! - Homepage Website Design - Coding not required- Winner to complete further pages

Hi all,

We're looking at redesigning our current website with a few adjustments to other pages but the main adjustments will be on the homepage which is what this design request is for. Please note : any of these ideas can be changed if you have something particularly different / special in mind etc.

P.S Coding is not required, just a design.

- Our website -

Our website is simply a price comparison website that allows customers to find companies within their area at the best price. The products available are mostly related to the vehicle trade and all refer to vinyl. This includes the likes of vehicle window tint, vehicle colour change vehicle wrap, vehicle signage as well as other cosmetic vinyl modifications. We allow the customer to search for their product within their chosen area and receive a list of companies who supply their product within that area. From here they can compare prices and view further details on the company.

- What we're looking to do -

We're looking first of all to adjust how the website homepage is displayed, this includes adding images and adjusting the colours that are explained below:

First of all, we look to spread out each of the 12 products (which can be seen on the website as it stands) and add an image to each of the products (all being spaced out as shown in our sketch)

We've been told the website looks too busy so we're thinking if we adjust the colours to more simplier neutral colours as well as the main focus of the website being on the 12 images, that would be great.

- Logo + Banner -

Logo to remain top left although banner may be removed / adjusted to make simplier.

- Colours -

Adjustments - Colours shades
We want the website to still look exciting but simplify the colours. Needs to be kept up to date with the colours / textures etc (bright colours to highlight keypoints)
We're still looking to use either blue or orange or maybe both to highlight these keypoints but the main website to be light colours and maybe even black on white background. The entire homepage can be adjusted colour wise if you feel it fits into your theme including menu bars, banners etc. The key is to get this right with being not too overpowering with the colours but still look interesting and up to date.

- 1 - 4 steps banner - (text may change)

This sits just under the logo and explains to the user how easy the website is to use and the steps they need to take. This may change to a 1 - 5 steps but we're looking to have this designed once the overall colours / theme of the website is sorted.

- 12 images - 4 x 3

This is the main focus of the website and will be the main focus of what the customer sees first of all. This will be where they select their product and then underneath, enter their postcode and distance they would like to search within. As explained further up, we have some of the product images available so if you can where possible add these to the design and then duplicate the images on those we currently don't have available.

- 12 Images -Titles -

These titles will be in this order from left to right and etc

- Colour Change Wrap
- Printed Vehicle Wrap
- Window Tint
- Headlight Tint
- Vehicle Signage
- Shop Signage
- Roof Vinyl Wrap
- Bonnet Vinyl Wrap
- Carbon Fibre Vinyl
- Stickerbomb Vinyl
- Clear Protective Vinyl
- Wheel Refurb

Text to be quite large, centered and with the o to the left of the title. Short titles like 'Window Tint' should fit on one line in the middle of the box where as titles such as ' Stickerbomb Vinyl Wrap' should have the 'Stickerbomb Vinyl' on the first line with the 'Wrap' on the line below. The background of this text is up to experient, might be worth just a simple colour or it might be worth using a bright blue or orange to keep in with the theme of the logo etc.

These will also have the circle tick box to the left of the title (as on the current website) where the customer clicks to select the product they have available.
We were also thinking that if when the customer ticks the circle on their selected box, the box is highlighted in some way to show this.

- Search Block -

This will appear under the 12 images and allows the customer to input their postcode and distance for the search criteria. Colours on this can of course be adjusted to keep in theme with the website.

- Under the 12 Images -

- Block underneath the 12 images and search block -

To the left will be some key bullet points about the website - maybe 4 or 5 with a green tick to the left of this. Background colour will probably be best to be a light colour, possibly grey.

Then to the right of this will appear 4 images, 2 before and 2 after when applying these products. Images to be used aren't fully decided on and we would like this stage of the design left to the end when the rest of the theme etc have been decided on.

Attached images are as follows :
- How the website looks as it stands
- The fold line on the website (obviously important)
- Our rough sketch of how we'd like the website homepage to look.
- We have 7 of the images ready that are all attached in this one file. Please duplicate the images on those that currently don't have the image available.

We will also be requesting a website developer to put this into action if our current designer falls through so please feel free to contact us if potentially interested.

The layout can change if you can think of something particular different / unique that works with this design. The main idea is to not only get the 12 products on view to the viewers but also the keypoints and before and after images.

Any questions, please ask away as we're bound to have forgotten a few things.

Thanks and good luck!

Hi all, keep the designs coming.

We haven't quite seen that extra special design we're after. As stated, we're after something fairly simple to suit the youth as well as the middle aged but we're also after something that bit special.

Colours to concentrate on are still and orange etc although feel free to use other colours if you have anything special in mind.

Please experience and we'll give you our honest feedback.

Many thanks all and good luck!

Hi all, this is a message to all the designers.

Some good designs coming in but we're still after that something special for the website design. Keep the designs coming and please feel free to experiment with the design colours, layout etc.

The basic principle of the website needs to remain regarding the 12 products, search within block and 4 steps all appearing on the homepage.

The 4 steps seems to work best when it's got text as well as some simple images next to this.

A variation with the product titles with how to display this, some designers have gone with a simple white background whereas others have gone with colours. Please experiment here and where possible, add a contract / texture to the colour. Please remember the product titles needs to be clear, centured and with the circle tick box to the left of it. 

We're after a fairly simple design although we need it to look 21st century, up to date as well as interesting. The key points straight away are the 4 steps as well as the 12 products so try to guide the viewer to these areas a little.

White background behind the 12 images seems to be a much, although a light colour could possibly work.

The keypoints underneath these 12 products are too very important as it outlines what we do etc. Tick colour can vary.

Next to these keypoints will be the 'before' and 'after' images, these images needs to be fairly small and ensure there is white background around the image itself.

Good luck all and any questions, feel free to ask away.

Thanks!

Hi,

 Thank you for your time and effort with these designs, we are very nearly there with the design but we've thought of something that may work for the homepage. A curved arrow from step 1 pointing to the products, this may or may not work but feel free to give it a go.

Many thanks,

Thank you to everyone for your time and efforts with the design. It's hugely appreciated so thank you all once again.

Wish you all the luck in the future.

```html
<!DOCTYPE html>
<html lang="en">
<head>
<meta charset="utf-8">
<title>WrapScout – Compare Vinyl Installers</title>
<link href="https://fonts.googleapis.com/css2?family=Arimo:ital,wght@0,400;0,700;1,400;1,700&display=swap" rel="stylesheet">
<style>
:root{
  --page:#e6e6e6;
  --white:#ffffff;
  --navy:#44598f;
  --navy-light:#6478b0;
  --orange:#f7941d;
  --ink:#333333;
  --muted:#555555;
  --bar:#cfcfcf;
  --panel:#efefef;
  --thumb:#8b9ccb;
  --tick:#5fbf2a;
}
*{box-sizing:border-box;margin:0;padding:0}
html,body{width:1017px;height:1200px;overflow:hidden}
body{background:var(--page);font-family:"Arimo",Arial,sans-serif;color:var(--ink);position:relative}
.sheet{position:absolute;left:45px;top:0;width:919px;height:1200px;background:var(--white);box-shadow:0 0 8px rgba(0,0,0,.25)}
.brand{position:absolute;left:80px;top:44px;display:flex;align-items:center;gap:10px}
.brand-dot{width:30px;height:30px;border-radius:50%;background:var(--orange)}
.brand-name{font-size:30px;font-weight:700;color:var(--navy);letter-spacing:1px}
.main-nav{position:absolute;left:474px;top:93px;display:flex;font-size:12px;color:var(--ink)}
.main-nav a{color:inherit;text-decoration:none;padding:0 13px;border-left:1px solid var(--ink);line-height:12px}
.main-nav a:first-child{border-left:0;padding-left:0;color:var(--orange)}
.steps-band{position:absolute;left:0;top:122px;width:1017px;height:141px;background:linear-gradient(90deg,var(--navy) 0%,var(--navy-light) 50%,var(--navy) 100%)}
.steps-intro{position:absolute;left:104px;top:16px;color:var(--white);font-style:italic;font-size:18px;line-height:25px}
.step{position:absolute;top:74px;display:flex;align-items:center;gap:6px;color:var(--white);font-weight:700;font-style:italic;font-size:13.5px;line-height:18px}
.step-num{width:44px;height:44px;border-radius:50%;background:var(--orange);border:2px solid #ffd08a;display:flex;align-items:center;justify-content:center;font-size:32px;font-style:normal;box-shadow:0 1px 3px rgba(0,0,0,.3)}
.search-bar{position:absolute;left:47px;top:263px;width:917px;height:30px;background:var(--bar);display:flex;align-items:center;font-size:13.5px;box-shadow:0 2px 3px rgba(0,0,0,.2)}
.search-bar .lead{margin-left:147px;font-style:italic;margin-right:18px}
.search-bar .label{font-size:13.5px;margin-right:6px}
.search-bar input{height:18px;border:1px solid #bbb;font:10px "Arimo",sans-serif;padding:0 4px;color:#aaa;margin-right:12px}
.search-bar button{background:var(--orange);color:var(--white);border:0;font:700 14px "Arimo",sans-serif;padding:2px 8px;margin-left:0}
.product{position:absolute;width:196px;border-top:3px solid var(--navy)}
.product-art{height:122px;background:linear-gradient(180deg,#f2f2f2,#dadada)}
.art-van{background:linear-gradient(180deg,#eef0f3 0%,#9cb6d8 35%,#4b8a2d 70%,#dcdcdc 100%)}
.art-car{background:radial-gradient(circle at 50% 55%,#56b33c 0 30%,#ececec 55%)}
.art-white{background:radial-gradient(circle at 50% 55%,#f8f8f8 0 35%,#e2e2e2 70%)}
.art-shop{background:linear-gradient(180deg,#f3f3f3 0 30%,#2b2b2b 30% 90%,#e7e7e7 90%)}
.art-silver{background:radial-gradient(circle at 50% 50%,#a9a9a9 0 30%,#ebebeb 60%)}
.art-sticker{background:radial-gradient(circle at 50% 40%,#d8643c 0 18%,#f0f0f0 45%)}
.product-title{height:25px;background:var(--navy);color:var(--white);font-weight:700;font-size:12.5px;display:flex;align-items:center;padding-left:8px;gap:7px}
.radio{width:9px;height:9px;border-radius:50%;background:#e8e8e8;border:1px solid #999}
.info{position:absolute;left:64px;top:914px;width:876px;height:204px;background:var(--panel);border-top:2px solid var(--navy);border-bottom:2px solid var(--navy)}
.info h2{position:absolute;font-weight:400;font-style:italic;font-size:21px;color:var(--ink)}
.points{position:absolute;left:22px;top:50px;list-style:none}
.points li{display:flex;align-items:flex-end;gap:2px;height:35px;font-style:italic;font-size:14px;color:var(--muted)}
.thumb{position:absolute;width:146px;height:50px;background:var(--thumb)}
.thumb-label{position:absolute;font-size:13.5px;color:var(--ink)}
.footer{position:absolute;left:45px;top:1156px;width:919px;height:44px;background:var(--navy)}
</style>
</head>
<body>
<div class="sheet"></div>

<header>
  <div class="brand"><span class="brand-dot"></span><span class="brand-name">WrapScout</span></div>
  <nav class="main-nav">
    <a href="#">HOME</a><a href="#">ABOUT US</a><a href="#">CONTACT US</a><a href="#">BLOG</a><a href="#">LIST YOUR COMPANY</a>
  </nav>
</header>

<section class="steps-band">
  <p class="steps-intro">Compare Professional Installers Today<br>With These Four Easy Steps...</p>
  <div class="step" style="left:133px"><span class="step-num">1</span><span>Select Chosen<br>Product</span></div>
  <div class="step" style="left:313px"><span class="step-num">2</span><span>Input Postcode<br>Distance &amp; Search</span></div>
  <div class="step" style="left:511px"><span class="step-num">3</span><span>Compare Companies<br>&amp; Prices</span></div>
  <div class="step" style="left:727px"><span class="step-num">4</span><span>Contact Chosen<br>Company</span></div>
</section>

<form class="search-bar">
  <span class="lead">...Or Search &amp; &amp; Save in Seconds!</span>
  <span class="label">SEARCH WITHIN</span>
  <input style="width:100px" value="Enter Miles">
  <span class="label">OF</span>
  <input style="width:100px" value="">
  <button type="button">SEARCH</button>
</form>

<main>
  <div class="product" style="left:69px;top:323px"><div class="product-art art-van" role="img" aria-label="Van with full colour change wrap"></div><div class="product-title"><span class="radio"></span>COLOR CHANGE WRAP</div></div>
  <div class="product" style="left:292px;top:323px"><div class="product-art art-van" role="img" aria-label="Van with printed vehicle wrap"></div><div class="product-title"><span class="radio"></span>PRINTED VEHICLE WRAP</div></div>
  <div class="product" style="left:517px;top:323px"><div class="product-art art-car" role="img" aria-label="Two green hatchbacks with tinted windows"></div><div class="product-title"><span class="radio"></span>WINDOW TINT</div></div>
  <div class="product" style="left:744px;top:323px"><div class="product-art art-car" role="img" aria-label="Two green hatchbacks with tinted headlights"></div><div class="product-title"><span class="radio"></span>HEADLIGHT TINTING</div></div>

  <div class="product" style="left:69px;top:517px"><div class="product-art art-white" role="img" aria-label="White van with company signage"></div><div class="product-title"><span class="radio"></span>VEHICLE SIGNAGE</div></div>
  <div class="product" style="left:292px;top:517px"><div class="product-art art-shop" role="img" aria-label="Shop front with window signage"></div><div class="product-title"><span class="radio"></span>SHOP SIGNAGE</div></div>
  <div class="product" style="left:517px;top:517px"><div class="product-art art-silver" role="img" aria-label="Silver car with black vinyl roof"></div><div class="product-title"><span class="radio"></span>ROOF VINYL WRAP</div></div>
  <div class="product" style="left:744px;top:517px"><div class="product-art art-silver" role="img" aria-label="Silver car with black vinyl bonnet"></div><div class="product-title"><span class="radio"></span>BONNET VINYL WRAP</div></div>

  <div class="product" style="left:69px;top:715px"><div class="product-art art-van" role="img" aria-label="Van with carbon fibre vinyl"></div><div class="product-title"><span class="radio"></span>CARBON FIBER VINYL</div></div>
  <div class="product" style="left:292px;top:715px"><div class="product-art art-sticker" role="img" aria-label="White sports car with stickerbomb bonnet"></div><div class="product-title"><span class="radio"></span>STICKERBOMB VINYL</div></div>
  <div class="product" style="left:517px;top:715px"><div class="product-art art-van" role="img" aria-label="Van with clear protective vinyl"></div><div class="product-title"><span class="radio"></span>CLEAR PROTECTIVE VINYL</div></div>
  <div class="product" style="left:744px;top:715px"><div class="product-art art-van" role="img" aria-label="Van with refurbished wheels"></div><div class="product-title"><span class="radio"></span>WHEEL REFURB</div></div>
</main>

<section class="info">
  <h2 style="left:25px;top:19px">How Can We Help You?</h2>
  <ul class="points">
    <li><svg width="30" height="26" viewBox="0 0 30 26"><path d="M2 14 L11 23 L28 2 L11 17 Z" fill="var(--tick)"/></svg>Input Text Here Input Text Here Input Text Here</li>
    <li><svg width="30" height="26" viewBox="0 0 30 26"><path d="M2 14 L11 23 L28 2 L11 17 Z" fill="var(--tick)"/></svg>Input Text Here Input Text Here Input Text Here</li>
    <li><svg width="30" height="26" viewBox="0 0 30 26"><path d="M2 14 L11 23 L28 2 L11 17 Z" fill="var(--tick)"/></svg>Input Text Here Input Text Here Input Text Here</li>
    <li><svg width="30" height="26" viewBox="0 0 30 26"><path d="M2 14 L11 23 L28 2 L11 17 Z" fill="var(--tick)"/></svg>Input Text Here Input Text Here Input Text Here</li>
  </ul>
  <h2 style="left:408px;top:19px">Learn More About These Tranformations...</h2>
  <div class="thumb" style="left:462px;top:59px" role="img" aria-label="Before image"></div>
  <div class="thumb" style="left:686px;top:59px" role="img" aria-label="After image"></div>
  <div class="thumb" style="left:462px;top:117px" role="img" aria-label="Before image"></div>
  <div class="thumb" style="left:686px;top:117px" role="img" aria-label="After image"></div>
  <span class="thumb-label" style="left:502px;top:179px">BEFORE</span>
  <span class="thumb-label" style="left:738px;top:179px">AFTER</span>
</section>

<footer class="footer"></footer>
</body>
</html>
```